Flyer für Anbieter von Geduldsspielen und kniffligen Denksportaufgaben
Zielgruppe
Die Knobelfunken-Kammer ist ein prunkvoll geschmückter Tisch mit wundersamen Geduldsspielen und kniffligen Denksportaufgaben ganz im Retro-Style der viktorianischen Zeit. Man kann die Knobelfunken-Kammer mieten für Veranstaltungen wie Hochzeiten, Jubiläen oder Firmen-/Mitarbeiter-Events
Aufgabenstellung
Der Flyer muss die Wiedererkennung mit der Website https://www.knobelfunkenkammer.de erfüllten. Texte siehe dort. Bildmaterial ist vorhanden und wird gestellt.

```html
<!DOCTYPE html>
<html lang="de">
<head>
<meta charset="utf-8">
<title>Knobelfunken-Kammer – Flyer</title>
<link href="https://fonts.googleapis.com/css2?family=Dancing+Script:wght@500;700&family=Poppins:wght@400;600;700&display=swap" rel="stylesheet">
<style>
:root{
  --stage:#8c8c8c;
  --linen:#ddd3c1;
  --brown:#4a3a22;
  --ink:#3f3020;
  --red:#a8222c;
  --cream:#efe3cc;
  --black:#070606;
  --badge:#2a47a8;
  --tent:#efedeb;
}
*{margin:0;padding:0;box-sizing:border-box}
html,body{width:1200px;height:1117px;overflow:hidden;background:var(--stage)}
body{position:relative;font-family:"Poppins",sans-serif;color:var(--ink)}
.page{position:absolute;top:165px;width:551px;height:786px;background:var(--linen);overflow:hidden}
.page--front{left:39px}
.page--back{left:609px}
.abs{position:absolute}
.script{font-family:"Dancing Script",cursive;font-weight:500;white-space:nowrap}
.kicker{top:24px;left:0;width:100%;text-align:center;color:var(--red);font-weight:700;font-size:11.5px}
.title{top:40px;left:0;width:100%;text-align:center;font-size:50px;line-height:1;color:var(--ink)}
.swash{position:absolute}
.gear{border-radius:50%;background:radial-gradient(circle,#8d8169 0 22%,transparent 23% 36%,#7d705a 37%,#5d5140 100%)}
.tagline{left:166px;top:126px;width:340px;font-size:11.6px;font-weight:700;line-height:1.4}
.band{position:absolute;left:0;width:100%;background:var(--brown)}
.photo{position:absolute;left:0;width:100%}
.photo--stand{top:187px;height:218px;background:linear-gradient(100deg,#6d4a35 0%,#c4285a 38%,#b72a55 55%,#2c2426 80%,#e9e5e2 100%)}
.watch{left:280px;top:375px;width:264px;height:163px;background:radial-gradient(ellipse at 75% 40%,#c9b9a3 0 25%,#8a5a3c 40%,transparent 70%)}
.intro{left:53px;top:440px;width:222px;font-size:9.6px;line-height:1.3}
.intro strong{display:block;margin-top:8px;font-weight:700}
.footer{position:absolute;left:0;top:544px;width:100%;height:242px;background:var(--black)}
.thumbs{position:absolute;left:30px;top:17px;display:flex;gap:6px}
.thumb{width:119px;height:92px;border:2px solid var(--red);border-radius:7px}
.cta{left:0;width:100%;text-align:center;top:122px;font-size:44px;line-height:1;color:var(--cream)}
.cta span{display:inline-block;transform:translateX(-20px)}
.badge{left:444px;top:125px;width:58px;height:58px;border-radius:50%;background:var(--badge);border:3px solid #dfe4f4}
.ask{left:0;width:100%;text-align:center;top:187px;font-size:12px;font-weight:700;color:var(--cream)}
.contact{left:0;width:100%;top:212px;display:flex;justify-content:center;gap:22px;font-size:12.5px;font-weight:700;color:var(--cream)}
.contact span{display:flex;align-items:center;gap:8px}
.contact svg{width:12px;height:12px}
.photo--couple{top:0;height:294px;background:
  linear-gradient(to bottom,var(--tent) 0 18%,rgba(239,237,235,0) 42%),
  linear-gradient(110deg,#e9e6e4 0%,#cfc3b6 30%,#1b1719 45%,#6e1420 65%,#ebe9e7 85%,#f3f1ef 100%)}
.back-title{left:32px;top:28px;font-size:26px;line-height:1.2;color:var(--ink)}
.back-gear{left:400px;top:237px;width:134px;height:132px}
.benefit-head{left:43px;top:324px;font-size:26px;line-height:1.2;color:var(--ink)}
.benefit{position:absolute;display:flex;gap:12px;font-size:9.4px;font-weight:700;line-height:1.3}
.benefit svg{flex:none;width:23px;height:23px}
.credits{left:290px;top:487px;width:230px;font-size:9.6px;line-height:1.3}
.footer--back .cta{top:116px}
.footer--back .badge{top:124px}
.footer--back .ask{top:181px}
.footer--back .contact{top:206px}
</style>
</head>
<body>

<section class="page page--front">
  <p class="abs kicker">Als Hochzeitsspiel, für Firmenevents oder Geburtstage:</p>
  <h1 class="abs title script">Knobelfunken-Kammer</h1>
  <svg class="swash" style="left:165px;top:95px" width="330" height="14" viewBox="0 0 330 14"><path d="M2 9 C90 3 220 2 328 4 L326 8 C230 8 120 10 4 12 Z" fill="#a8222c"/></svg>
  <div class="band" style="top:168px;height:22px"></div>
  <div class="photo photo--stand" role="img" aria-label="Foto: geschmückter Knobeltisch mit Lichterkette, Holzschild und lachender Gastgeberin mit Hut"></div>
  <div class="band" style="top:403px;height:18px"></div>
  <div class="abs gear" style="left:25px;top:108px;width:136px;height:128px" role="img" aria-label="Illustration: bronzenes Zahnrad"></div>
  <p class="abs tagline">Ein prunkvoll geschmückter Tisch mit wundersamen Geduldsspielen und kniffligen Denksportaufgaben.</p>
  <div class="abs watch" role="img" aria-label="Illustration: kupferne Taschenuhr mit Kette"></div>
  <p class="abs intro">Ganz im Retro-Style der viktorianischen Zeit sorgen Sie mit der Knobelfunken-Kammer auf Ihrer Veranstaltung für einen außergewöhnlichen „Hingucker" und beste Unterhaltung.<strong>Garantiert: Keine Langeweile!</strong></p>
  <footer class="footer">
    <div class="thumbs">
      <div class="thumb" style="background:linear-gradient(#c9b4a0,#7a5a44)" role="img" aria-label="Foto: Holzkisten mit Knobelspielen"></div>
      <div class="thumb" style="background:linear-gradient(90deg,#e8ddd6,#b54a60,#5b6f8c)" role="img" aria-label="Foto: Gäste beim Knobeln"></div>
      <div class="thumb" style="background:linear-gradient(#8a6a50,#a2283a)" role="img" aria-label="Foto: Schubladen mit Rätseln auf rotem Samt"></div>
      <div class="thumb" style="background:linear-gradient(135deg,#e6d9c6,#a58740)" role="img" aria-label="Foto: goldene Schere als Geduldsspiel"></div>
    </div>
    <p class="abs cta script"><span>Worauf warten?</span></p>
    <div class="abs badge" role="img" aria-label="Auszeichnungsplakette"></div>
    <p class="abs ask">Stellen Sie hier Ihre unverbindliche Anfrage!</p>
    <div class="abs contact">
      <span><svg viewBox="0 0 12 12"><circle cx="6" cy="6" r="6" fill="#efe3cc"/><path d="M3.6 3.2l1.2-.3.7 1.5-.8.6a4 4 0 0 0 2.3 2.3l.6-.8 1.5.7-.3 1.2C6 8.6 3.4 6 3.6 3.2z" fill="#070606"/></svg>knobelei@knobelfunkenkammer.de</span>
      <span><svg viewBox="0 0 12 12"><circle cx="6" cy="6" r="6" fill="#efe3cc"/><rect x="3" y="4" width="6" height="4.2" fill="none" stroke="#070606" stroke-width=".8"/><path d="M3 4l3 2.3L9 4" fill="none" stroke="#070606" stroke-width=".8"/></svg>+49 0171 5550192</span>
    </div>
  </footer>
</section>

<section class="page page--back">
  <div class="photo photo--couple" role="img" aria-label="Foto: Gastgeberpaar in viktorianischen Kostümen auf einer Hochzeitsmesse"></div>
  <p class="abs back-title script">Knobelfunken-Kammer</p>
  <div class="band" style="top:290px;height:18px"></div>
  <div class="abs gear back-gear" role="img" aria-label="Illustration: bronzenes Zahnrad"></div>
  <h2 class="abs benefit-head script">Die Vorteile für Sie und Ihre Gäste</h2>
  <svg class="swash" style="left:65px;top:360px" width="290" height="10" viewBox="0 0 290 10"><path d="M2 7 C90 3 200 2 288 3 L286 6 C200 6 100 8 4 9 Z" fill="#a8222c"/></svg>

  <div class="benefit" style="left:43px;top:386px;width:230px">
    <svg viewBox="0 0 24 24"><path d="M12 21C5 15 2 12 2 8a5 5 0 0 1 10-1 5 5 0 0 1 10 1c0 4-3 7-10 13z" fill="none" stroke="#3f3020" stroke-width="1.5"/></svg>
    <p>Die Knobelfunken-Kammer ist der perfekte Lückenfüller, zum Beispiel zwischen Programmpunkten auf Hochzeiten oder Firmenevents.</p>
  </div>
  <div class="benefit" style="left:43px;top:444px;width:240px">
    <svg viewBox="0 0 24 24"><path d="M4 4h12a3 3 0 0 1 3 3v4a3 3 0 0 1-3 3H9l-4 3v-3H4a3 3 0 0 1-3-3V7a3 3 0 0 1 3-3z M20 9a3 3 0 0 1 3 3v4a3 3 0 0 1-3 3v3l-4-3h-5" fill="none" stroke="#3f3020" stroke-width="1.3"/></svg>
    <p>Ihre Gäste kommen ins Gespräch beim gemeinsamen Grübeln.</p>
  </div>
  <div class="benefit" style="left:43px;top:480px;width:230px">
    <svg viewBox="0 0 24 24"><circle cx="12" cy="12" r="10" fill="none" stroke="#3f3020" stroke-width="1.4"/><circle cx="8.5" cy="10" r="1" fill="#3f3020"/><circle cx="15.5" cy="10" r="1" fill="#3f3020"/><path d="M7.5 14.5a5 5 0 0 0 9 0" fill="none" stroke="#3f3020" stroke-width="1.4"/></svg>
    <p>Die kleinen Knobeleien zu meistern macht Spaß und sorgt für echte Unterhaltung.</p>
  </div>
  <div class="benefit" style="left:290px;top:386px;width:240px">
    <svg viewBox="0 0 24 24"><path d="M12 3C7 3 3 6 3 11c0 4 2 7 5 8v2h8v-2c3-1 5-4 5-8 0-5-4-8-9-8zM12 3v16M8 7c1 2 0 4-2 5M16 7c-1 2 0 4 2 5M8 14c2 0 3 1 4 2M16 14c-2 0-3 1-4 2" fill="none" stroke="#3f3020" stroke-width="1.2"/></svg>
    <p>Wer die Lösung nicht findet, dem werden die Tricks verraten: Das sorgt immer wieder für großes Staunen.</p>
  </div>
  <div class="benefit" style="left:290px;top:432px;width:230px">
    <svg viewBox="0 0 24 24"><circle cx="12" cy="12" r="10" fill="none" stroke="#3f3020" stroke-width="1.4"/><circle cx="8.5" cy="10" r="1" fill="#3f3020"/><path d="M14 10h3" stroke="#3f3020" stroke-width="1.4"/><path d="M7.5 14.5a5 5 0 0 0 9 0" fill="none" stroke="#3f3020" stroke-width="1.4"/></svg>
    <p>Kurzum: Die Knobelfunken-Kammer ist der ideale Spaß für Ihre Gäste!</p>
  </div>
  <p class="abs credits">Lena Falk and Dr. Jonas Rieder have extensive experience in program planning at festivals and celebrations.</p>

  <footer class="footer footer--back">
    <div class="thumbs">
      <div class="thumb" style="background:linear-gradient(#b5302f,#9a8874)" role="img" aria-label="Foto: Knobelspiele auf dem Tisch"></div>
      <div class="thumb" style="background:linear-gradient(#c0294e,#7a5740)" role="img" aria-label="Foto: Holzfässer mit Bechern"></div>
      <div class="thumb" style="background:linear-gradient(90deg,#d8c7bb,#a33247,#2a2224)" role="img" aria-label="Foto: Gastgeberin am Knobeltisch"></div>
      <div class="thumb" style="background:linear-gradient(90deg,#d0cccc,#6e5f58,#2b2222)" role="img" aria-label="Foto: Gast löst ein Rätsel mit dem Gastgeber"></div>
    </div>
    <p class="abs cta script"><span>Worauf warten?</span></p>
    <div class="abs badge" role="img" aria-label="Auszeichnungsplakette"></div>
    <p class="abs ask">Stellen Sie hier Ihre unverbindliche Anfrage!</p>
    <div class="abs contact">
      <span><svg viewBox="0 0 12 12"><circle cx="6" cy="6" r="6" fill="#efe3cc"/><path d="M3.6 3.2l1.2-.3.7 1.5-.8.6a4 4 0 0 0 2.3 2.3l.6-.8 1.5.7-.3 1.2C6 8.6 3.4 6 3.6 3.2z" fill="#070606"/></svg>knobelei@knobelfunkenkammer.de</span>
      <span><svg viewBox="0 0 12 12"><circle cx="6" cy="6" r="6" fill="#efe3cc"/><rect x="3" y="4" width="6" height="4.2" fill="none" stroke="#070606" stroke-width=".8"/><path d="M3 4l3 2.3L9 4" fill="none" stroke="#070606" stroke-width=".8"/></svg>+49 0171 5550192</span>
    </div>
  </footer>
</section>

</body>
</html>
```